labels loose leaf tea business

I am in need of a label redo! I have attatched a couple of our old logo labels (still currently using these labels) also i have our new logo that we have loaded on the website feel free to look. www.brewlark.com i bought the business a year ago and have been wanting to get a new look for a minimal cost.we use the labels that are 4' by 3 1/3' on the bags that hold 100 grams the bag is 5.25"x 8 "stand up pouch and the smaller bag which is 4.25x 6.75" we have used a 2x2 label (which doesn't have room for as much detail. the bags are a matte silver at the time.
i am considering going to either a matte white or there is an aqua co lour not sure if that would work or there is a nice white or silver grey rice paper looking bag i am getting prices.
i would consider a larger label format on this bag as well for retail i need my logo the address and the telephone and website all the ingredients as well as tea type and caffiene content i like to include a short description of the tea, as well as country of origin could be fun.. i have included the steep time and possibly this is something to take into consideration is to make a small info graphic of the steep times that is the same sticker to go on the reverse side of each bag the same.could include the address and website... as you can see my bags have had a different color banner per the type of tea Which my customers are used to that idea pink means fruit black is abrown label blue is herbal etc.
to say what is my style is kind of hard for me i included the two pieces of art work from Northgate Printworks ...the coffee label i liked the bottom part simple and straight forward, (i could also look into seeing how much it would cost to heat stamp my logo on each bag) the second one i do kind of like had drawn also sort of vintage the new logo being aqua and grey to me is fresh and light....really i don't like busy or fussy or Victorian i like a bit unusual ( like the sticker on the kraft paper bag! but it could be a pain to put on straight every time i think the one on the biscotti (art image 3) is kind of neat how its applied the other way...
Anyway my market is some retail/ farmers markets etc.. and website.as well as our own retail shop.we have about 90 kinds of tea so i need to be able to edit and print these myself as to hold stock on labels is not cost effective.
i also should say we use the 4 oz metal tins which i use the same labels size as the large bag but mayb we could design it to fit around the whole tin.
well i hope this is enough info for you and i am super excited to see the products you come up with

Project Deadline Extended Reason: Thank you for taking time to look at my design project. i feel to extend the time as i have never done this before and realize some of you may have better ideas then i have and i feel like you may need more time as well and i have also been talking to some product manufacturers such as the pouches and printer and label makers, i think if possible i will head in the direction of getting a stock label printed where the basic information is pre-printed and i can just change the product detail AS needed.This however may throw a different twist on the labels as i'm not sure that the colored banner such as i had is the way to go.i can see potential in a couple of the designs.However much i wish i could get my logo preprinted ont he bags its not an option at this point its too pricy...so yay keep the designs coming we aren't finished yet! Added Sunday, February 12, 2017

Project Deadline Extended Reason: i am giving five more days, my reason being i have been ill and dont feel like i have the energy to give my full attention too the project as well as we have a wedding on the weekend...i see some close competiton here....and am getting excited as well as nervous as how i will really pick between so many cool designs Added Thursday, February 16, 2017

Project Deadline Extended
Reason: one more deadline... giving some of you designers a chance to get them in that had started on the designs please know this is the last extension and i am not super super excited about any of them yet.....i am looking for a label that can be changed up for the different tea types such as Tamsin provided so far.... so let your imaginations go and become creative, thanks for all the awesome effort so far.....

Target Market(s)

website,farmers markets, retail...seems to cover a broad spectrum of ages

Industry/Entity Type

Business

Colors
86cfc6

Requirements
Must have
• Brewlark is the name
• www.brewlark.com website
• packaged and blended in Canada
• Cedarvale Alberta
• 403-718-2045
• 100 grams or 50 grams
• Tea type and name
• the steeping time and water temp and amount of tea
Nice to have
• Discover loose leaf tea at its brightest i s on the logo
• wouldn't have to have it there could take off and put somewhere else
• description of the tea as seen on the old tea labels i would like included

```html
<!DOCTYPE html>
<html lang="en">
<head>
<meta charset="utf-8">
<title>Brewlark — Berry Breeze label set</title>
<link rel="stylesheet" href="https://fonts.googleapis.com/css2?family=Arimo:wght@400;700&family=Marcellus+SC&display=swap">
<style>
  :root {
    --teal: #5fb0a1;
    --teal-deep: #4d9c8e;
    --teal-soft: #86cfc6;
    --ink: #1f2a28;
    --paper: #ffffff;
    --stage: #e9e7e4;
    --rule: #7dbfb3;
    --leaf-grey: #b9bdbc;
  }
  * { box-sizing: border-box; margin: 0; padding: 0; }
  html, body { width: 1200px; height: 585px; overflow: hidden; }
  body { background: var(--stage); font-family: "Arimo", Arial, sans-serif; color: var(--ink); position: relative; }

  /* front pennant label */
  .front-label {
    position: absolute; left: 130px; top: 10px;
    width: 380px; height: 565px; background: var(--paper);
    clip-path: polygon(0 0, 100% 0, 100% 88%, 50% 100%, 0 88%);
    box-shadow: 0 2px 6px rgba(0,0,0,.12);
    text-align: center;
  }
  .pattern-panel {
    height: 170px;
    background: linear-gradient(135deg, var(--teal) 0%, #6fbcae 50%, var(--teal) 100%);
  }
  .brand { padding-top: 18px; height: 100px; }
  .brand-name {
    font-family: "Marcellus SC", Georgia, serif; color: var(--teal);
    font-size: 42px; line-height: 1; letter-spacing: 1px;
    display: inline-flex; align-items: center; gap: 10px;
  }
  .brand-dot { width: 12px; height: 12px; border-radius: 50%; background: var(--leaf-grey); }
  .tagline {
    font-family: "Marcellus SC", Georgia, serif; color: var(--teal);
    font-size: 11px; letter-spacing: .6px; margin-top: 8px;
  }
  .tagline-curve { display: block; margin: 2px auto 0; }

  .name-band { background: var(--teal); color: #fff; padding: 9px 0 8px; }
  .tea-name { font-family: "Marcellus SC", Georgia, serif; font-weight: 400; font-size: 30px; letter-spacing: 1.5px; line-height: 1.1; }
  .tea-type { font-family: "Marcellus SC", Georgia, serif; font-size: 11px; letter-spacing: .8px; margin-top: 2px; }

  .description { font-size: 15px; line-height: 1.3; padding: 9px 30px 0; }
  .dots { color: var(--teal); font-size: 9px; letter-spacing: 5px; margin: 5px 0; }
  .origin {
    border-top: 1px solid var(--rule); border-bottom: 1px solid var(--rule);
    margin: 0 14px; padding: 4px 0;
    font-family: "Marcellus SC", Georgia, serif; font-size: 11px; letter-spacing: .6px;
  }
  .ingredients {
    text-align: left; padding: 7px 22px 0;
    font-family: "Marcellus SC", Georgia, serif; font-size: 10px; line-height: 1.4; letter-spacing: .4px;
  }
  .ingredients b { font-weight: 400; font-size: 11px; }
  .weight { margin-top: 6px; color: var(--teal); font-family: "Marcellus SC", Georgia, serif; }
  .weight-amount { font-size: 11px; display: block; margin-top: 1px; }
  .servings { font-size: 8px; display: block; margin-top: 2px; }

  /* back steeping sticker */
  .back-label {
    position: absolute; left: 620px; top: 128px;
    width: 500px; height: 330px; background: var(--paper);
    box-shadow: 0 2px 6px rgba(0,0,0,.12);
    padding: 26px 22px 0; text-align: center;
  }
  .steep-guide { display: flex; height: 150px; }
  .steep-step { flex: 1; display: flex; flex-direction: column; align-items: center; gap: 18px; padding-top: 6px; border-left: 1px solid var(--rule); }
  .steep-step:first-child { border-left: 0; }
  .steep-label { font-family: "Marcellus SC", Georgia, serif; font-size: 15px; letter-spacing: .6px; }
  .contact-bar {
    margin-top: 10px; background: var(--teal); color: #fff;
    display: flex; justify-content: space-between; padding: 8px 14px;
    font-size: 13px; letter-spacing: .3px;
  }
  .back-brand { margin-top: 24px; height: auto; padding-top: 0; }
  .back-brand .brand-name { font-size: 30px; }
  .back-brand .tagline { font-size: 9px; margin-top: 6px; }
</style>
</head>
<body>

<section class="front-label" aria-label="Front pouch label">
  <div class="pattern-panel" role="img" aria-label="Teal and white geometric tile pattern"></div>

  <header class="brand">
    <div class="brand-name"><span class="brand-dot"></span>Brewlark</div>
    <p class="tagline">Discover loose leaf tea at its brightest</p>
    <svg class="tagline-curve" width="260" height="8" viewBox="0 0 260 8" aria-hidden="true"><path d="M2 6 Q130 -2 258 6" fill="none" stroke="#b9bdbc" stroke-width="1.2"/></svg>
  </header>

  <div class="name-band">
    <h1 class="tea-name">Berry Breeze</h1>
    <p class="tea-type">Caffeine free loose / fruit tea</p>
  </div>

  <p class="description">Sweet sugary notes of butterscotch blend in perfect harmony with the decadent characteristics of pu-erh.</p>
  <div class="dots">◆◆◆◆◆◆ &nbsp; ◆◆◆◆◆◆</div>
  <p class="origin">Packaged and blended in Canada</p>

  <p class="ingredients"><b>Ingredients:</b> luxury natural dried apple pieces, hibiscus, rosehip natural dried orange, calendula petals, natural flavors.</p>

  <div class="weight">
    <svg width="22" height="18" viewBox="0 0 22 18" aria-hidden="true">
      <path d="M3 7h12v4a5 5 0 0 1-5 5H8a5 5 0 0 1-5-5z" fill="none" stroke="#5fb0a1" stroke-width="1.3"/>
      <path d="M15 8.5h2a2 2 0 0 1 0 4h-2.3" fill="none" stroke="#5fb0a1" stroke-width="1.3"/>
      <path d="M7 2c-1 1.3 1 2 0 3.5M10.5 2c-1 1.3 1 2 0 3.5" fill="none" stroke="#5fb0a1" stroke-width="1"/>
    </svg>
    <span class="weight-amount">100gr</span>
    <span class="servings">38-50 servings</span>
  </div>
</section>

<section class="back-label" aria-label="Back steeping sticker">
  <div class="steep-guide">
    <div class="steep-step">
      <span class="steep-label">Boiling (212°)</span>
      <svg width="110" height="40" viewBox="0 0 110 40" aria-hidden="true">
        <circle cx="20" cy="20" r="12" fill="#5fb0a1"/>
        <rect x="30" y="16" width="74" height="8" rx="4" fill="none" stroke="#5fb0a1" stroke-width="2"/>
        <rect x="30" y="18" width="34" height="4" fill="#5fb0a1"/>
      </svg>
    </div>
    <div class="steep-step">
      <span class="steep-label">5 minutes</span>
      <svg width="44" height="44" viewBox="0 0 44 44" aria-hidden="true">
        <circle cx="22" cy="22" r="18" fill="none" stroke="#5fb0a1" stroke-width="2.5"/>
        <path d="M22 11v11l8 6" fill="none" stroke="#5fb0a1" stroke-width="2.5" stroke-linecap="round"/>
      </svg>
    </div>
    <div class="steep-step">
      <span class="steep-label">1 ½ tsp per 8 oz</span>
      <svg width="110" height="40" viewBox="0 0 110 40" aria-hidden="true">
        <path d="M6 20h56" stroke="#5fb0a1" stroke-width="4" stroke-linecap="round"/>
        <ellipse cx="82" cy="20" rx="20" ry="11" fill="#5fb0a1"/>
      </svg>
    </div>
  </div>

  <div class="contact-bar">
    <span>Cedarvale Alberta</span>
    <span>403-718-2045</span>
    <span>www.brewlark.com</span>
  </div>

  <footer class="brand back-brand">
    <div class="brand-name"><span class="brand-dot"></span>Brewlark</div>
    <p class="tagline">Discover loose leaf tea at its brightest</p>
  </footer>
</section>

</body>
</html>
```